Childcare Centre trifold brochure

Design a contemporary trifold brochure for a childcare centre that meets Australian printing requirements with supplied content, logo's, fonts and photo's. Please refer to the attached DL flyer front and back for similar possible style and content.

Target Market(s)

Families

Industry/Entity Type

Childcare

Requirements
Must have
• refer attached content, photo's, logo's and examples. Colours should be same as Pantone purple and green and or variations of. Refer attached dl flyer example.

```html
<!DOCTYPE html>
<html lang="en">
<head>
<meta charset="utf-8">
<title>Childcare Centre Trifold – Inside Spread</title>
<link rel="stylesheet" href="https://fonts.googleapis.com/css2?family=Fira+Sans:ital,wght@0,400;0,500;0,600;1,500&display=swap">
<style>
  :root {
    --purple-deep: #9b3591;
    --purple-mid: #b34ea3;
    --purple-light: #cf7fbf;
    --green: #3aaa35;
    --ink: #222222;
    --white: #ffffff;
    --frame: #e4e4e4;
    --photo-earth: #7d6a4c;
    --photo-grass: #6f7a45;
    --photo-deck: #8a4a3a;
  }
  * { box-sizing: border-box; margin: 0; padding: 0; }
  html, body { width: 1200px; height: 934px; overflow: hidden; background: var(--white); }
  body { font-family: "Fira Sans", Arial, sans-serif; position: relative; }

  .spread {
    position: absolute; left: 14px; top: 14px; width: 1172px; height: 906px;
    border: 1px solid var(--frame); overflow: hidden;
  }
  .sky { position: absolute; left: -14px; top: -14px; width: 1200px; height: 934px; }

  .block { position: absolute; width: 330px; font-size: 14.4px; line-height: 23.7px; }
  .on-purple { color: var(--white); font-weight: 500; }
  .body-copy { color: var(--ink); }
  .body-copy p + p { margin-top: 23.7px; }
  .source { font-weight: 600; }

  .photo { position: absolute; }
  .photo--kitchen { left: 36px; top: 140px; width: 265px; height: 193px;
    background: linear-gradient(160deg, var(--photo-earth), var(--photo-deck) 60%, #b65a8a); }
  .photo--hammer { left: 419px; top: 44px; width: 165px; height: 194px;
    background: linear-gradient(170deg, var(--photo-earth), var(--photo-grass)); }
  .photo--saw { left: 601px; top: 44px; width: 145px; height: 194px;
    background: linear-gradient(170deg, #8c7a5e, #b7a98c); }

  .green-quotes { position: absolute; left: 36px; top: 536px; width: 340px;
    color: var(--green); font-style: italic; font-weight: 500; font-size: 17.6px; line-height: 23.6px; }
  .green-quotes p + p { margin-top: 19px; }

  .lead-quote { font-weight: 500; color: var(--ink); }
  .closing-quote { position: absolute; left: 815px; top: 708px; width: 340px;
    font-style: italic; font-weight: 500; font-size: 14.4px; line-height: 23.7px;
    color: var(--ink); text-align: center; }
  .closing-quote cite { display: block; text-align: left; font-style: italic; }
</style>
</head>
<body>
<div class="spread">
  <svg class="sky" viewBox="0 0 1200 934" aria-hidden="true">
    <defs>
      <radialGradient id="skyGlow" cx="0.5" cy="0.25" r="0.6">
        <stop offset="0" stop-color="var(--purple-light)"/>
        <stop offset="0.6" stop-color="var(--purple-mid)"/>
        <stop offset="1" stop-color="var(--purple-deep)"/>
      </radialGradient>
    </defs>
    <path fill="url(#skyGlow)" d="M14,14 H1186 V268
      Q1133,230 1080,275 Q1030,262 980,310 Q940,290 900,330 Q865,318 835,360
      Q810,372 800,400 Q775,412 750,445 Q715,418 680,460 Q650,428 620,470
      Q580,440 540,478 Q495,448 448,492 Q396,440 344,500 Q304,462 264,505
      Q244,480 224,500 Q198,452 172,495 Q90,455 14,500 Z"/>
  </svg>

  <div class="block on-purple" style="left:36px; top:38px;">
    Children’s confidence increased, and they had heightened levels of self-belief, positive attitude, independence and demonstrated an increased ability to take initiatives.
  </div>
  <div class="photo photo--kitchen" role="img" aria-label="Toddlers in sun hats chopping vegetables on an outdoor deck"></div>
  <div class="block on-purple" style="left:36px; top:348px;">
    Children who play regularly in natural settings are sick less often. Mud, sand, water, leaves, sticks, pine cones and gum nuts can help to stimulate children's immune system as well as their imagination.
  </div>

  <div class="photo photo--hammer" role="img" aria-label="Child in a purple hat using a hand drill on wood outdoors"></div>
  <div class="photo photo--saw" role="img" aria-label="Child in gloves sawing a block of wood in the sand"></div>
  <div class="block on-purple" style="left:418px; top:252px;">
    Children who spend more time outside tend to be more physically active and are less likely to be overweight. They are more resistant to stress; have lower incidence of behavioural disorders, anxiety and depression; and have a higher measure of
  </div>

  <div class="block on-purple" style="left:813px; top:40px; width:340px;">
    Children who play in natural settings play in more diverse, imaginative and creative ways and show improved language and collaboration skills They also have more positive feelings about each other.
  </div>

  <div class="green-quotes">
    <p>“Providing outdoor opportunities for learning is a critical priority for parents, teachers and the wider community”</p>
    <p>“Outdoor learning was added to the Australian Curriculum in 2015, however just 34% of teachers surveyed taught outdoors for 15 minutes or more”</p>
    <p style="margin-top:27px;">“Nature ignites passion, inspiration, creativity &amp; purpose and plays an important role in the cognitive, emotional and physical development of children”</p>
  </div>

  <div class="block body-copy" style="left:420px; top:490px;">
    <p><span class="source">Source: Roots and Branches: Outdoor Play for Growing Minds’ report, Published July 2017</span><br>
    Since 2015, throughout each school term our educators run free lessons for all ages in the following: yoga, meditation, sign language, Spanish, German, Malaysian, Sri Lankan Culture, Sustainability, Noongar Culture &amp; Sport.</p>
    <p>The sign language is a particular hit with the mothers as the babies are able to sign to their parents when they are hungry or need to go to the toilet before they even start talking.</p>
    <p>The first five years of a child’s development are the most crucial with 90% of their brain synapsis being formed by this time.</p>
  </div>

  <div class="block body-copy" style="left:815px; top:350px; width:345px;">
    <p class="lead-quote">“Early childhood is the most important time for brain development. It is the time in a child's life where they start building their brain connections and therefore, ultimately,<br>the work we do will shape their life forever”.</p>
    <p>We believe that the best developmental outcomes occur when children who wander, wonder and play are also learning. It happens when children’s interests and passions are respected and nurtured and when educators shift their agenda away from imparting knowledge that we consider worthy, to showing children that we value their curiosity, problem solving, questions, and theories.</p>
  </div>

  <blockquote class="closing-quote">
    “Passion is lifted from the earth itself by the muddy hands of the young;<br>
    it travels along grass stained sleeves to the heart.<br>
    If we are going to save environmentalism and the environment,<br>
    we must also save an endangered indicator species: the child in nature.”
    <cite>Ellis Marlowe</cite>
  </blockquote>
</div>
</body>
</html>
```